Kessler MD Summit Primary Care Business Card

Need a business card for a medical clinic targeting VIP patients. Should portray an upscale feeling. Simple, clean design. Logo and colors need to be incorporated into card. Clinic colors are gray/ silver, blues, white same as logo.
Clinic is a cash only VIP service clinic targeting higher income patients.
Tagline: "Where every patient comes first - Unhurried care"

Target Market(s)

VIP, upscale

Industry/Entity Type

Medical

Contact Information for Business Card

Would like to use for cards with raised print or metallic highlight.

Requirements
Must have
• Incorporate logo, Use colors in logo
Nice to have
• Metallic detail
Should not have
• too much details or colors, other stock photos or designs

```html
<!DOCTYPE html>
<html lang="en">
<head>
<meta charset="utf-8">
<title>Kessler MD Summit Primary Care – Business Card</title>
<link rel="stylesheet" href="https://fonts.googleapis.com/css2?family=Open+Sans:wght@400&family=Tinos:wght@400;700&display=swap">
<style>
  :root {
    --page-bg: #ecebe8;
    --card-grey: #8f989c;
    --brand-navy: #3c4f67;
    --brand-silver: #9aa1a5;
    --paper-white: #ffffff;
    --ink-white: #ffffff;
  }
  html, body {
    margin: 0;
    width: 1200px;
    height: 900px;
    overflow: hidden;
    background: var(--page-bg);
  }
  .canvas {
    position: relative;
    width: 1200px;
    height: 900px;
  }
  .card {
    position: absolute;
    box-shadow: 0 6px 18px rgba(0,0,0,0.18);
    overflow: hidden;
  }

  /* Contact side */
  .card-back {
    left: 78px;
    top: 35px;
    width: 587px;
    height: 362px;
    background: var(--card-grey);
    color: var(--ink-white);
  }
  .brand-band {
    position: absolute;
    left: 0;
    top: 0;
    width: 150px;
    height: 100%;
    background: var(--brand-navy);
  }
  .holder {
    position: absolute;
    right: 35px;
    top: 44px;
    text-align: right;
  }
  .holder-name {
    font-family: "Tinos", serif;
    font-weight: 700;
    font-size: 21px;
    letter-spacing: 0.3px;
    margin: 0;
    line-height: 1.1;
  }
  .holder-title {
    font-family: "Open Sans", sans-serif;
    font-size: 15.5px;
    margin: 2px 0 0;
    padding-right: 4px;
  }
  .contact-list {
    position: absolute;
    right: 35px;
    top: 180px;
    margin: 0;
    padding: 0;
    list-style: none;
    font-family: "Open Sans", sans-serif;
    font-size: 15.8px;
    line-height: 21.5px;
    text-align: right;
  }
  .contact-list li {
    display: flex;
    justify-content: flex-end;
    align-items: center;
    gap: 7px;
  }
  .contact-list svg {
    width: 12px;
    height: 12px;
    fill: var(--ink-white);
  }
  .address {
    position: absolute;
    right: 35px;
    top: 280px;
    margin: 0;
    font-family: "Open Sans", sans-serif;
    font-style: normal;
    font-size: 15.8px;
    line-height: 21.5px;
    text-align: right;
  }

  /* Brand side */
  .card-front {
    left: 388px;
    top: 505px;
    width: 567px;
    height: 352px;
    background: var(--paper-white);
  }
  .brand-dot {
    position: absolute;
    left: 253px;
    top: 94px;
    width: 60px;
    height: 60px;
    border-radius: 50%;
    background: var(--brand-silver);
  }
  .brand-name {
    position: absolute;
    left: 0;
    top: 190px;
    width: 100%;
    margin: 0;
    text-align: center;
    font-family: "Tinos", serif;
    text-transform: uppercase;
  }
  .brand-name-primary {
    display: flex;
    align-items: center;
    justify-content: center;
    gap: 12px;
    font-size: 24px;
    line-height: 28px;
    letter-spacing: 0.8px;
    color: var(--brand-silver);
  }
  .brand-name-primary::before,
  .brand-name-primary::after {
    content: "";
    width: 36px;
    height: 2px;
    background: var(--brand-silver);
  }
  .brand-name-secondary {
    display: block;
    font-size: 21px;
    line-height: 26px;
    letter-spacing: 1px;
    color: var(--brand-navy);
  }
  .tagline-band {
    position: absolute;
    left: 0;
    bottom: 0;
    width: 100%;
    height: 70px;
    background: var(--card-grey);
    display: flex;
    align-items: center;
    justify-content: center;
  }
  .tagline {
    margin: 0;
    font-family: "Tinos", serif;
    font-weight: 700;
    font-size: 15.5px;
    letter-spacing: 0.6px;
    text-transform: uppercase;
    color: var(--ink-white);
  }
</style>
</head>
<body>
<main class="canvas">

  <section class="card card-back" aria-label="Business card, contact side">
    <div class="brand-band" role="img" aria-label="Navy brand band where the clinic emblem appears as a large decoration"></div>
    <div class="holder">
      <h1 class="holder-name">DANIEL REEVES</h1>
      <p class="holder-title">Managing Director</p>
    </div>
    <ul class="contact-list">
      <li>044-123 456 789
        <svg viewBox="0 0 12 12" aria-hidden="true"><path d="M3 0h6a1 1 0 0 1 1 1v10a1 1 0 0 1-1 1H3a1 1 0 0 1-1-1V1a1 1 0 0 1 1-1zm0.5 1.5v7.5h5V1.5z"/></svg>
      </li>
      <li>044-123 456 789
        <svg viewBox="0 0 12 12" aria-hidden="true"><path d="M0 4c0-2 2.5-3 6-3s6 1 6 3v1H9V3.5H3V5H0zM2 6h8l1 5H1z"/></svg>
      </li>
      <li>info@webname.com
        <svg viewBox="0 0 12 12" aria-hidden="true"><path d="M0 2h12v8H0zm1 1v.4l5 3.2 5-3.2V3zm0 1.6V9h10V4.6L6 7.8z"/></svg>
      </li>
      <li>www.websitename.com
        <svg viewBox="0 0 12 12" aria-hidden="true"><circle cx="6" cy="6" r="6"/></svg>
      </li>
    </ul>
    <address class="address">12345, Address Goes Here<br>Country Name, 123456.</address>
  </section>

  <section class="card card-front" aria-label="Business card, brand side">
    <span class="brand-dot" aria-hidden="true"></span>
    <p class="brand-name">
      <span class="brand-name-primary">Kessler MD</span>
      <span class="brand-name-secondary">Summit Primary Care</span>
    </p>
    <div class="tagline-band">
      <p class="tagline">Where every patient comes first - Unhurried care</p>
    </div>
  </section>

</main>
</body>
</html>
```